Electronics Recycling and IT Asset Disposition Flyer and Brochure Design

We need a 2 side A5 Flyer and 4 side A4 folder( brochure) for our electronics waste recycling and IT asset management and disposition business.
Our business provides free electronics waste recycling for companies, schools, learning institutions,councils, IT companies and government sectors. Many people are ignorant of responsible recycling of electronics which could harm our health if not treated properly.
The list of other services attached in the pdf.
We provide an end to end and tailored solution for our customers from collection, logistics, data sanitisation, remarketing and recycling.

The Flyer should create awareness of responsible electronics recycling and drive the audience to contact us or go to our website to learn more about the company and services.A brief list of services should also be included in the flyer.The goal is to get the audience to contact us to enquire more about our services.

The Brochure should include all the above plus provide more details about the company, processes, services,contact details (fb, linkedin,Twitter). The goal is to convert the audience to customers for recycling and provide other services as added services.

The final design for both flyer and brochure should communicate responsible recycling of electronic scrap and tailored solution for every organisation.

The company website is www.kelvora-scrap.com.au based in Australia. We serve clients nationwide.

Target Market(s)

IT companies, Corporate, schools and learning institutions, government sector

Industry/Entity Type

Recycling

Contact Information for Business Card

Name: Derek Ollinfeld
email: derek@kelvora-scrap.com.au
website: www.kelvora-scrap.com.au
mobile: +614 631 02957
Phone: 1300 64 2835

Font styles to use
Serif

Requirements
Must have
• I would like the designs to have more images and icons
Nice to have
Should not have
• none

```html
<!DOCTYPE html>
<html lang="en">
<head>
<meta charset="utf-8">
<title>Kelvora Scrap – Presentation Folder</title>
<link href="https://fonts.googleapis.com/css2?family=Source+Sans+3:wght@400;600;700&family=Oswald:wght@600&display=swap" rel="stylesheet">
<style>
  :root{
    --forest:#2f6a2f;
    --forest-deep:#245a25;
    --leaf:#3d7f35;
    --lime:#bde53a;
    --lime-soft:#b2dc2e;
    --ink:#2b2b2b;
    --paper:#ffffff;
    --stage:#e9e9e9;
  }
  *{box-sizing:border-box;margin:0;padding:0}
  html,body{width:1200px;height:1200px;overflow:hidden}
  body{background:var(--stage);font-family:"Source Sans 3",Arial,sans-serif;position:relative}

  .spread{position:absolute;left:294px;width:642px}
  .spread--outside{top:70px;height:558px}
  .spread--inside{top:734px;height:412px}

  .panel{position:absolute;top:0;width:321px;overflow:hidden}
  .panel--left{left:0}
  .panel--right{left:321px}

  .pocket{position:absolute;bottom:0;height:144px;background:var(--lime)}
  .pocket--left{left:0;width:316px}
  .pocket--right{left:326px;width:316px}
  .spread--inside .pocket{height:137px}

  /* outside back cover */
  .back-cover{height:414px;background:linear-gradient(160deg,var(--leaf) 0%,var(--forest) 40%,var(--forest-deep) 100%)}
  .back-cover__texture{position:absolute;left:0;top:180px;width:321px;height:234px;
    background:linear-gradient(180deg,rgba(36,90,37,0) 0%,rgba(20,60,22,.35) 100%)}
  .brand{font-weight:700;letter-spacing:.5px;line-height:1;text-align:center}
  .back-cover .brand{position:absolute;left:0;right:0;top:176px;color:var(--paper);font-size:30px}
  .back-cover__call{position:absolute;left:0;right:0;top:262px;text-align:center;color:var(--lime);font-size:17px;font-weight:600}
  .back-cover__addr{position:absolute;left:0;right:0;top:287px;text-align:center;color:var(--paper);font-size:9.5px;line-height:13px}

  /* outside front cover */
  .front-cover{height:414px;background:var(--paper)}
  .front-cover svg{position:absolute;left:0;top:0}
  .front-cover .brand{position:absolute;right:28px;top:36px;width:150px;color:var(--forest);font-size:30px}
  .cta{position:absolute;left:164px;top:240px;width:114px;height:114px;border-radius:50%;
    background:radial-gradient(circle at 50% 35%,#c9ef52 0%,var(--lime) 55%,#8fc21f 100%);
    border:5px solid var(--paper);display:flex;flex-direction:column;align-items:center;justify-content:center;
    font-family:"Oswald",Impact,sans-serif;color:var(--ink);line-height:1}
  .cta__small{font-size:16px}
  .cta__big{font-size:30px;margin-top:2px}
  .front-cover__web{position:absolute;right:24px;top:374px;color:var(--paper);font-size:10px;letter-spacing:2.4px}

  .pocket__stamp{position:absolute;left:0;right:0;text-align:center;color:var(--forest)}
  .pocket__stamp .brand{font-size:26px}
  .pocket__web{font-size:10px;letter-spacing:2.2px;color:var(--ink);margin-top:10px}
  .pocket--left .pocket__stamp{top:22px;transform:rotate(180deg);display:flex;flex-direction:column-reverse}
  .pocket--left .pocket__web{margin-top:0;margin-bottom:10px}
  .spread--inside .pocket--right .pocket__stamp{top:26px}

  /* inside */
  .inside-panel{height:275px;background:var(--paper)}
  .inside-panel--right{background:linear-gradient(90deg,#dcdcdc 0%,#f4f4f4 14%,var(--paper) 30%)}
</style>
</head>
<body>

<section class="spread spread--outside">
  <div class="panel panel--left back-cover">
    <div class="back-cover__texture" role="img" aria-label="Faint photo of circuit boards in dark green tint"></div>
    <div class="brand">Kelvora<br>Scrap</div>
    <p class="back-cover__call">Call us today at 1300 64 2835</p>
    <p class="back-cover__addr">18-22 Marlow Street, Greystanes 2145 NSW<br>www.kelvora-scrap.com.au</p>
  </div>

  <div class="panel panel--right front-cover">
    <svg width="321" height="414" viewBox="0 0 321 414">
      <defs>
        <linearGradient id="photoTone" x1="0" y1="0" x2="1" y2="1">
          <stop offset="0" stop-color="#c9b8a8"/>
          <stop offset=".5" stop-color="#e6e1dc"/>
          <stop offset="1" stop-color="#9aa0a4"/>
        </linearGradient>
        <linearGradient id="photoFade" x1="0" y1="0" x2="0" y2="1">
          <stop offset="0" stop-color="#fff" stop-opacity="1"/>
          <stop offset=".18" stop-color="#fff" stop-opacity="0"/>
        </linearGradient>
        <linearGradient id="greenBody" x1="0" y1="0" x2="0" y2="1">
          <stop offset="0" stop-color="#3f8536"/>
          <stop offset="1" stop-color="#245a25"/>
        </linearGradient>
      </defs>
      <rect x="0" y="122" width="270" height="292" fill="url(#photoTone)" role="img" aria-label="Photo of office team reviewing work at a computer"/>
      <rect x="0" y="122" width="270" height="292" fill="url(#photoFade)"/>
      <path d="M0,0 L22,0 C45,50 90,98 150,120 C90,110 35,80 0,50 Z" fill="var(--forest)"/>
      <path d="M321,194 C290,170 262,178 250,205 C230,255 150,330 0,414 L321,414 Z" fill="url(#greenBody)"/>
      <path d="M262,170 C290,185 290,220 250,260 C200,305 100,360 0,398 L0,408 C110,370 215,318 262,268 C300,228 298,188 262,170 Z" fill="var(--lime)"/>
      <path d="M0,414 C120,362 220,315 265,275 L268,282 C225,325 130,372 22,414 Z" fill="var(--paper)"/>
    </svg>
    <div class="brand">Kelvora<br>Scrap</div>
    <div class="cta"><span class="cta__small">CONTACT US</span><span class="cta__big">TODAY</span></div>
    <p class="front-cover__web">www.kelvora-scrap.com.au</p>
  </div>

  <div class="pocket pocket--left">
    <div class="pocket__stamp">
      <div class="brand">Kelvora Scrap</div>
      <p class="pocket__web">www.kelvora-scrap.com.au</p>
    </div>
  </div>
  <div class="pocket pocket--right"></div>
</section>

<section class="spread spread--inside">
  <div class="panel panel--left inside-panel"></div>
  <div class="panel panel--right inside-panel inside-panel--right"></div>
  <div class="pocket pocket--left"></div>
  <div class="pocket pocket--right">
    <div class="pocket__stamp">
      <div class="brand">Kelvora Scrap</div>
      <p class="pocket__web">www.kelvora-scrap.com.au</p>
    </div>
  </div>
</section>

</body>
</html>
```